BELU Safety Poster

We need a safety poster designed that we can provide to our members to put up on the wall of their factories. It needs to be clear and concise and simple but also that they are aware it is provided by us. We would like the poster to be in line with our branding companies, you can view these on our website www.tarnvalehub.com A3 size please

All files are here https://www.quillstash.com/sh/p8ve2mz7tqs4lr9/QQhuTrwc-LPMaxRuF83Zcf5H1?n=47193052

```html
<!DOCTYPE html>
<html lang="en">
<head>
<meta charset="utf-8">
<title>BELU Safety Poster – Heat Stress</title>
<link href="https://fonts.googleapis.com/css2?family=Creepster&family=Jolly+Lodger&family=Oswald:wght@500;600&family=Marcellus+SC&display=swap" rel="stylesheet">
<style>
  :root {
    --poster-yellow: #ffe01b;
    --poster-edge: #e9c600;
    --band-dark: #1c1c1c;
    --band-mid: #3a3a3a;
    --title-red: #e3161b;
    --ink-black: #111111;
    --bullet-brown: #9a5a2a;
    --warning-red: #d9141a;
    --ribbon-white: #ffffff;
    --badge-orange: #f7821e;
    --brand-purple: #7b4f92;
    --flame-orange: #f58a1f;
    --flame-red: #e0301e;
  }
  * { margin: 0; padding: 0; box-sizing: border-box; }
  html, body { width: 848px; height: 1200px; overflow: hidden; background: var(--poster-yellow); }
  .poster {
    position: relative; width: 848px; height: 1200px; overflow: hidden;
    background: var(--poster-yellow);
    box-shadow: inset 0 0 0 3px var(--poster-edge);
  }
  .top-ribbon { position: absolute; left: 42px; top: 0; width: 144px; height: 168px; }
  .title-band {
    position: absolute; left: -90px; top: 142px; width: 1030px; height: 116px;
    transform: rotate(-19deg); transform-origin: center;
    background: repeating-linear-gradient(45deg, var(--band-dark) 0 6px, var(--band-mid) 6px 9px);
    border-top: 4px solid #8a8a8a; border-bottom: 4px solid #8a8a8a;
    box-shadow: 0 4px 10px rgba(0,0,0,.45);
    display: flex; align-items: center; justify-content: center;
  }
  .title-band h1 {
    font-family: "Creepster", cursive; font-weight: 400;
    font-size: 104px; letter-spacing: 0; line-height: 1; white-space: nowrap;
    color: var(--title-red); -webkit-text-stroke: 2px #3a0000;
    text-shadow: 2px 3px 0 #000;
    margin-top: 14px;
    transform: scaleX(.78);
  }
  .tips { position: absolute; left: -8px; top: 318px; width: 848px; list-style: none; text-align: center; }
  .tips li {
    font-family: "Jolly Lodger", cursive; font-size: 43px; line-height: 61px;
    letter-spacing: 1.5px; color: var(--ink-black); text-transform: uppercase; white-space: nowrap;
  }
  .tips li::before { content: "\2726"; color: var(--bullet-brown); font-size: 18px; margin-right: 16px; vertical-align: middle; }
  .thermometer-art {
    position: absolute; left: 48px; top: 588px; width: 312px; height: 420px;
    border-radius: 40% 45% 30% 35%;
    background: radial-gradient(ellipse at 55% 55%, #d8b690 0 28%, var(--flame-orange) 42%, var(--flame-red) 62%, rgba(224,48,30,0) 72%);
  }
  .signs { position: absolute; left: 330px; top: 648px; width: 510px; }
  .signs h2 {
    font-family: "Oswald", sans-serif; font-weight: 600; font-size: 27px;
    color: var(--warning-red); text-transform: uppercase; letter-spacing: .3px; white-space: nowrap;
    text-shadow: 1px 1px 0 #7a0000;
  }
  .signs ul { list-style: none; margin: 16px 0 0 62px; }
  .signs li {
    font-family: "Oswald", sans-serif; font-weight: 500; font-size: 21px; line-height: 33px;
    color: var(--warning-red); text-transform: uppercase; letter-spacing: .8px; white-space: nowrap;
  }
  .signs li::before { content: "\2726"; color: var(--warning-red); font-size: 15px; margin-right: 14px; }
  .urgent-note {
    position: absolute; left: 348px; top: 824px; width: 490px; text-align: center;
    font-family: "Oswald", sans-serif; font-weight: 500; font-size: 19px; line-height: 25px;
    color: var(--warning-red); text-transform: uppercase; letter-spacing: .6px; white-space: nowrap;
  }
  .credit-banner { position: absolute; left: 252px; top: 996px; width: 342px; height: 204px; }
  .credit-banner svg { position: absolute; inset: 0; }
  .credit-line {
    position: absolute; left: 0; top: 56px; width: 342px; text-align: center;
    font-family: "Marcellus SC", serif; font-size: 24px; color: var(--brand-purple); white-space: nowrap;
  }
  .credit-rule { position: absolute; left: 14px; top: 94px; width: 314px; height: 2px; background: var(--brand-purple); }
  .member-mark { position: absolute; left: 16px; top: 106px; display: flex; align-items: center; gap: 16px; }
  .member-mark .dot { width: 86px; height: 86px; border-radius: 50%; background: var(--brand-purple); }
  .member-mark .name {
    font-family: "Marcellus SC", serif; font-size: 18px; line-height: 21px;
    color: var(--brand-purple); width: 200px;
  }
</style>
</head>
<body>
<main class="poster">
  <svg class="top-ribbon" viewBox="0 0 144 168" aria-hidden="true">
    <path d="M0 0 H144 V168 L72 128 L0 168 Z" fill="var(--ribbon-white)"/>
    <circle cx="72" cy="66" r="50" fill="var(--badge-orange)" stroke="#1a1a1a" stroke-width="3"/>
    <rect x="64" y="34" width="12" height="46" rx="6" fill="none" stroke="#1a1a1a" stroke-width="3"/>
    <circle cx="70" cy="86" r="10" fill="#c0141a" stroke="#1a1a1a" stroke-width="3"/>
    <rect x="67.5" y="50" width="5" height="30" fill="#c0141a"/>
    <text x="84" y="54" font-family="Oswald, sans-serif" font-weight="600" font-size="18" fill="#1a1a1a">C</text>
  </svg>

  <div class="title-band"><h1>Heat Stress Isn't Cool</h1></div>

  <ul class="tips">
    <li>Drink plenty of water</li>
    <li>Take breaks</li>
    <li>Wear light clothing when appropriate</li>
    <li>Monitor work mates for signs of heat stress</li>
  </ul>

  <div class="thermometer-art" role="img" aria-label="Illustration of a wooden thermometer with a red reading engulfed in flames"></div>

  <section class="signs">
    <h2>Signs of heat stress or heat exhaustion</h2>
    <ul>
      <li>Feeling sick, weak or clumsy / dizzy.</li>
      <li>Cramps can also be caused by heat</li>
      <li>Discomfort from heat rash</li>
    </ul>
  </section>

  <p class="urgent-note">** If you have profuse sweating, weakness,<br>nausea or vomiting, headaches and muscle spasms<br>then stop work immediately and seek help.</p>

  <div class="credit-banner">
    <svg viewBox="0 0 342 204" aria-hidden="true">
      <path d="M0 0 L171 40 L342 0 V204 H0 Z" fill="var(--ribbon-white)"/>
    </svg>
    <p class="credit-line">This is an BELU Safety Poster</p>
    <div class="credit-rule"></div>
    <div class="member-mark">
      <span class="dot"></span>
      <span class="name">Tarnvale Moulders Guild</span>
    </div>
  </div>
</main>
</body>
</html>
```